Musician Business Card Design

I am freelance Double Bass player based in New York. I play every style of music, from Pop music to Contemporary Classical Music. I am also a private Bass and music theory teacher. What I hope to communicate with my business card is that I am a reliable and competent musician. I like designs with geometric patterns, I am very found of mandalas, so maybe we could incorporate that into the idea. I am looking for a design that will be easy on the eyes, and will have something that will make people want to keep it.
Thanks for all your help.

Industry/Entity Type

Business

Contact Information for Business Card

Tomas Verhel
+1 (347) 555-0193
marquet.tv@quillbox.net

```html
<!DOCTYPE html>
<html lang="en">
<head>
<meta charset="utf-8">
<title>Tomas Verhel — Business Card</title>
<link href="https://fonts.googleapis.com/css2?family=Allura&family=Titillium+Web:wght@300&display=swap" rel="stylesheet">
<style>
  :root {
    --backdrop: #c6c8c7;
    --card: #ffffff;
    --name-purple: #5b2470;
    --contact-grey: #8d8d8d;
    --mandala-teal: #5fd0d6;
    --mandala-sky: #4fa7dc;
    --mandala-blue: #2f63b8;
    --mandala-navy: #2a2f6a;
  }
  html, body {
    margin: 0;
    padding: 0;
    width: 1200px;
    height: 1000px;
    overflow: hidden;
    background: var(--backdrop);
  }
  .business-card {
    position: absolute;
    left: 60px;
    top: 184px;
    width: 1080px;
    height: 632px;
    background: var(--card);
    box-shadow: 0 2px 10px rgba(0,0,0,0.12);
    overflow: hidden;
  }
  .mandala-art {
    position: absolute;
    inset: 0;
    width: 1080px;
    height: 632px;
  }
  .card-identity {
    position: absolute;
    left: 0;
    right: 0;
    top: 210px;
    text-align: center;
  }
  .card-name {
    margin: 0;
    font-family: "Allura", cursive;
    font-weight: 400;
    font-size: 92px;
    line-height: 1;
    color: var(--name-purple);
  }
  .card-contact {
    margin: 38px 0 0;
    font-family: "Titillium Web", sans-serif;
    font-weight: 300;
    font-size: 37px;
    line-height: 1;
    color: var(--contact-grey);
    letter-spacing: 0.2px;
  }
  .card-contact .divider {
    margin: 0 12px;
  }
</style>
</head>
<body>
  <main class="business-card">
    <svg class="mandala-art" viewBox="0 0 1080 632" role="img" aria-label="Watercolour mandala of blue, teal and navy petals, split by a white band">
      <defs>
        <radialGradient id="mandala-fill" cx="538" cy="327" r="302" gradientUnits="userSpaceOnUse">
          <stop offset="0" stop-color="var(--mandala-teal)"/>
          <stop offset="0.35" stop-color="var(--mandala-sky)"/>
          <stop offset="0.75" stop-color="var(--mandala-blue)"/>
          <stop offset="1" stop-color="var(--mandala-navy)"/>
        </radialGradient>
        <clipPath id="mandala-caps">
          <rect x="0" y="0" width="1080" height="178"/>
          <rect x="0" y="451" width="1080" height="181"/>
        </clipPath>
      </defs>
      <circle cx="538" cy="327" r="302" fill="url(#mandala-fill)" clip-path="url(#mandala-caps)"/>
    </svg>
    <section class="card-identity">
      <h1 class="card-name">Tomas Verhel</h1>
      <p class="card-contact">+1 (347) 555-0193<span class="divider">|</span>marquet.tv@quillbox.net</p>
    </section>
  </main>
</body>
</html>
```